Webshop Template

For our Webstore in UK we need a complete Template,
shoppingcart is Magento, the Shop is focussed on Download software,

the name: Appvaultdepot.co.uk

Check out some other good stores, like lumawerk.de

for example the Page from 

www.brenvik.co.uk or

www.lumawerk.de

www.tastenhugo.de

www.klickrabatt.de

The Logodesign which are in Consideration

http://www.artmosaiq.com/design/5520817/logo-design-by-tomasz7kv

http://www.artmosaiq.com/design/5518360/logo-design-by-luisgaviota

http://www.artmosaiq.com/design/5517245/logo-design-by-kestrel-works

http://www.artmosaiq.com/design/5516093/logo-design-by-zumbiloft

http://www.artmosaiq.com/design/5515471/logo-design-by-tivaro

http://www.artmosaiq.com/design/5514902/logo-design-by-blue-fern-graphics-

Target Market(s)

B2C - Consumer Marcet

Industry/Entity Type

Shop

```html
<!DOCTYPE html>
<html lang="en">
<head>
<meta charset="utf-8">
<title>Appvaultdepot.co.uk – Webshop</title>
<link rel="stylesheet" href="https://fonts.googleapis.com/css2?family=Questrial&family=Arimo:wght@400;700&display=swap">
<style>
:root{
  --bg:#ececec;
  --panel:#ffffff;
  --panel-edge:#dedede;
  --orange:#f08a24;
  --orange-light:#f6a04a;
  --text:#333333;
  --muted:#555555;
  --ink:#111111;
  --grey-btn:#6b6b6b;
  --box-blue:#1f4f96;
  --box-yellow:#f5be1e;
}
*{margin:0;padding:0;box-sizing:border-box}
html,body{width:1200px;height:878px;overflow:hidden}
body{background:radial-gradient(ellipse at 50% 40%,#f6f6f6 0%,var(--bg) 70%);font-family:"Arimo",Arial,sans-serif;color:var(--text);position:relative}
.abs{position:absolute}
.panel{position:absolute;background:var(--panel);border:1px solid var(--panel-edge);border-radius:6px}
.gothic{font-family:"Questrial",sans-serif}

/* top utility */
.top-links{left:750px;top:5px;font-size:8px;color:var(--muted);display:flex;gap:18px}
.top-links span:nth-child(4){margin-left:14px}
.top-links span:nth-child(5){margin-left:8px}
.side-btn{position:absolute;left:1129px;width:80px;height:33px;background:var(--grey-btn);border-radius:5px;color:#fff;font-weight:700;font-size:11px;display:flex;align-items:center;padding-left:9px;gap:7px}
.side-btn svg{flex:none}

/* header */
.header{left:161px;top:18px;width:878px;height:75px;background:#f3f3f3}
.brand{position:absolute;left:12px;top:18px;display:flex;align-items:center;gap:8px}
.brand-mark{width:34px;height:34px;border-radius:50%;background:#3a3a3a}
.brand-name{font-family:"Questrial",sans-serif;font-size:24px;color:#3a3a3a;letter-spacing:.5px}
.platform-tabs{position:absolute;left:291px;top:35px;display:flex;gap:14px;font-size:8px;color:var(--muted);align-items:center}
.platform-tabs .active{background:var(--orange);color:#fff;padding:2px 7px}
.search{position:absolute;left:280px;top:46px;width:292px;height:22px;background:#fff;border-radius:4px;border:1px solid #e4e4e4}
.search .cat{position:absolute;right:0;top:3px;height:16px;border-left:1px solid #ddd;padding:2px 8px;font-size:8px;color:var(--orange)}
.search-icon{position:absolute;left:580px;top:47px}
.welcome{position:absolute;right:9px;top:60px;font-size:11px;color:var(--muted)}

/* main nav */
.nav{left:161px;top:98px;width:878px;height:28px;background:#f3f3f3}
.nav-links{left:285px;top:106px;font-size:11px;color:var(--muted);display:flex;gap:52px}
.nav-home{left:211px;top:95px;width:50px;height:34px;background:linear-gradient(var(--orange-light),var(--orange));border-radius:6px;color:#fff;font-size:11px;text-align:center;line-height:34px}
.nav-home::after{content:"";position:absolute;left:19px;bottom:-6px;border:6px solid transparent;border-top-color:var(--orange);border-bottom:0}

/* tab header labels */
.tab-label{position:absolute;background:var(--panel);border-radius:5px 5px 0 0;font-family:"Questrial",sans-serif;color:var(--orange);font-size:13px;padding:6px 13px 0;height:24px}

/* categories */
.categories{left:161px;top:163px;width:136px;height:261px}
.cat-list{list-style:none;position:absolute;left:13px;top:10px;font-size:11px;line-height:15.8px;color:var(--text)}
.chev{position:absolute;color:var(--orange);font-size:11px}

/* slider */
.slider{left:304px;top:163px;width:710px;height:261px;border-top-left-radius:0}
.slider-tabs{position:absolute;left:382px;top:147px;display:flex;gap:36px;font-family:"Questrial",sans-serif;font-size:13px;color:var(--text)}
.product-art{position:absolute;border-radius:4px;background:linear-gradient(90deg,var(--box-blue) 0 35%,var(--box-yellow) 35% 65%,var(--box-blue) 65%)}
.slide-title{position:absolute;left:430px;top:20px;font-family:"Questrial",sans-serif;font-size:31px;color:#3a3a3a}
.slide-copy{position:absolute;left:430px;top:62px;width:240px;font-family:"Questrial",sans-serif;font-size:19px;line-height:16px;color:var(--ink)}
.slide-price{position:absolute;left:545px;top:204px;font-family:"Questrial",sans-serif;font-size:32px;font-weight:700;color:var(--ink)}
.featured{left:1013px;top:334px;width:24px;height:91px;background:var(--panel);border:1px solid var(--panel-edge);border-left:0;border-radius:0 6px 6px 0}
.featured span{position:absolute;left:5px;top:10px;writing-mode:vertical-rl;font-weight:700;font-size:13px;color:var(--orange);letter-spacing:.5px}

/* contact */
.contact{left:161px;top:447px;width:136px;height:117px}
.contact-info{position:absolute;left:13px;font-size:8px;line-height:10.5px;color:var(--text)}
.contact-info strong{font-weight:400;font-size:10.5px;display:block;margin-bottom:1px}

/* recommended */
.recommended{left:304px;top:447px;width:710px;height:117px;border-top-left-radius:0}
.rec-tabs{position:absolute;left:436px;top:432px;display:flex;gap:25px;font-family:"Questrial",sans-serif;font-size:13px;color:var(--text)}
.rec-item{position:absolute;top:29px}
.rec-item .product-art{left:0;top:0;width:68px;height:68px}
.rec-name{position:absolute;left:70px;top:-3px;white-space:nowrap;font-family:"Questrial",sans-serif;font-size:16px;color:#3a3a3a}
.rec-type{position:absolute;left:70px;top:17px;font-family:"Questrial",sans-serif;font-size:12px;color:var(--muted)}
.rec-price{position:absolute;left:105px;top:41px;font-family:"Questrial",sans-serif;font-size:21px;color:var(--ink)}

/* footer */
.footer-rule{left:0;width:1200px;height:0;border-top:1px dashed #d8d8d8}
.footer-col{position:absolute;top:634px}
.footer-col h3{font-family:"Questrial",sans-serif;font-weight:400;font-size:13px;color:var(--orange);margin-bottom:13px}
.footer-col ul{list-style:none;font-size:8px;line-height:12.3px;color:var(--text)}
.socials{display:flex;gap:8px}
.socials span{width:29px;height:29px;background:#888;border-radius:4px}
.newsletter-title{font-family:"Questrial",sans-serif;font-size:17px;color:var(--orange);margin:10px 0 10px -3px}
.newsletter{display:flex;align-items:center;gap:5px;margin-left:-3px}
.newsletter span{width:198px;height:22px;background:#fff;border-radius:3px;border:1px solid #e4e4e4}
.copyright{left:181px;top:785px;font-size:8px;color:var(--text)}
</style>
</head>
<body>

<div class="abs top-links"><span>My Account</span><span>My Wishlist</span><span>My Cart</span><span>Checkout</span><span>Log In</span></div>

<div class="side-btn" style="top:9px"><svg width="12" height="10" viewBox="0 0 12 10"><path d="M6 1 2 5l4 4M11 1 7 5l4 4" fill="none" stroke="var(--orange)" stroke-width="1.5"/></svg>Log in</div>
<div class="side-btn" style="top:50px"><svg width="12" height="10" viewBox="0 0 12 10"><path d="M6 1 2 5l4 4M11 1 7 5l4 4" fill="none" stroke="var(--orange)" stroke-width="1.5"/></svg>My Cart</div>

<header class="panel header">
  <div class="brand"><span class="brand-mark"></span><span class="brand-name">Appvaultdepot.co.uk</span></div>
  <div class="platform-tabs"><span class="active">Windows</span><span>Mac</span><span>iOS</span><span>Android</span></div>
  <div class="search"><span class="cat">Category &#8964;</span></div>
  <svg class="search-icon" width="20" height="22" viewBox="0 0 20 22"><circle cx="8" cy="8" r="6" fill="none" stroke="#999" stroke-width="3"/><path d="M12 13l5 6" stroke="#999" stroke-width="4" stroke-linecap="round"/></svg>
  <div class="welcome">Welcome to our software store!</div>
</header>

<nav>
  <div class="panel nav"></div>
  <div class="abs nav-links"><span>Windows</span><span>Mac</span><span>iOS</span><span>Android</span></div>
  <div class="abs nav-home">Home</div>
</nav>

<aside>
  <div class="tab-label" style="left:161px;top:140px;width:90px">Categories</div>
  <div class="panel categories">
    <ul class="cat-list">
      <li>Security</li><li>Business</li><li>Communications</li><li>Developer Tools</li><li>Games</li><li>Graphic Design</li><li>Productivity</li><li>Video</li><li>Security</li><li>Business</li><li>Communications</li><li>Developer Tools</li><li>Games</li><li>Graphic Design</li>
    </ul>
    <span class="chev" style="left:120px;top:8px">&#8250;</span>
    <span class="chev" style="left:120px;top:55px">&#8250;</span>
    <span class="chev" style="left:64px;top:238px;transform:rotate(90deg)">&#8250;</span>
  </div>

  <div class="tab-label" style="left:161px;top:431px;width:104px">Contact</div>
  <div class="panel contact">
    <div class="contact-info" style="top:19px"><strong>Support &amp; Order</strong>Phone: 00000000000<br>Mon-Fri 8-22 clock, Sat<br>10-20 clock</div>
    <div class="contact-info" style="top:71px"><strong>Customer Support</strong>Phone: 000000000000<br>Mon-Fri 9-18 clock</div>
  </div>
</aside>

<main>
  <div class="tab-label" style="left:304px;top:140px;width:91px;text-align:center">Windows</div>
  <div class="slider-tabs" style="left:420px"><span>Mac</span><span style="margin-left:-10px">iOS</span><span>Android</span></div>
  <section class="panel slider">
    <svg class="abs" style="left:20px;top:107px" width="14" height="38" viewBox="0 0 14 38"><path d="M12 1 2 19l10 18" fill="none" stroke="#222" stroke-width="1.5"/></svg>
    <div class="product-art" role="img" aria-label="Software box with a disc" style="left:113px;top:40px;width:150px;height:190px"></div>
    <h1 class="slide-title" style="font-weight:400">Software Name</h1>
    <p class="slide-copy">Lorem ipsum dolor sit amet, consectetur adipisicing elit, sed do eiusmod tempor incididunt ut labore et dolore magna aliqua.</p>
    <div class="slide-price">$999.99</div>
    <svg class="abs" style="left:675px;top:107px" width="14" height="38" viewBox="0 0 14 38"><path d="M2 1l10 18L2 37" fill="none" stroke="#222" stroke-width="1.5"/></svg>
  </section>
  <div class="abs featured"><span>FEATURED</span></div>

  <div class="tab-label" style="left:304px;top:429px;width:106px;padding-left:6px">Recommended</div>
  <div class="rec-tabs"><span>Offers</span><span>News</span><span>Popular Buys</span><span style="margin-left:-6px">Highly Rated</span></div>
  <section class="panel recommended">
    <div class="rec-item" style="left:26px"><div class="product-art" role="img" aria-label="Software box with a disc"></div><div class="rec-name">Software Name</div><div class="rec-type">Type</div><div class="rec-price">$999.99</div></div>
    <div class="rec-item" style="left:257px"><div class="product-art" role="img" aria-label="Software box with a disc"></div><div class="rec-name" style="left:74px">Software Name</div><div class="rec-type" style="left:74px">Type</div><div class="rec-price" style="left:108px">$999.99</div></div>
    <div class="rec-item" style="left:497px"><div class="product-art" role="img" aria-label="Software box with a disc"></div><div class="rec-name" style="left:74px">Software Name</div><div class="rec-type" style="left:74px">Type</div><div class="rec-price" style="left:108px">$999.99</div></div>
  </section>
</main>

<footer>
  <div class="abs footer-rule" style="top:615px"></div>
  <div class="footer-col" style="left:174px"><h3>Customer Service</h3><ul><li>Hotlines &amp; Contact · FAQ</li><li>Returns</li><li>Payments · Financing</li><li>Complaint &amp; Warranty</li><li>International customers</li><li>Terms · Privacy Policy</li><li>Imprint</li></ul></div>
  <div class="footer-col" style="left:349px"><h3>News</h3><ul><li>All News</li><li>Business Tech</li><li>Crave</li><li>Cutting Edge</li><li>Green Tech</li><li>Security</li><li>Wireless</li></ul></div>
  <div class="footer-col" style="left:474px"><h3>Downloads</h3><ul><li>Add Your Software</li><li>All Downloads</li><li>Mac</li><li>Android</li><li>iOS</li><li>Other Mobile</li><li>Software Deals</li></ul></div>
  <div class="footer-col" style="left:815px">
    <h3>Follow Us</h3>
    <div class="socials"><span></span><span></span><span></span><span></span></div>
    <div class="newsletter-title">Subscribe to NEWSLETTER</div>
    <div class="newsletter"><span></span><svg width="11" height="18" viewBox="0 0 11 18"><path d="M0 0l11 9-11 9z" fill="var(--orange)"/></svg></div>
  </div>
  <div class="abs copyright">Appvaultdepot © 1999 - 2013</div>
  <div class="abs footer-rule" style="top:825px"></div>
</footer>

</body>
</html>
```